Stationery Design Project - Tax Professionals/Chartered Accountants

The name of our firm is “Pellow Group” and our slogan is “Strategic Solutions”. You can also use the name "The Pellow Group" if it works better.

We are looking for a full stationery design: Letterhead, Business Card and With Compliments slip

We are looking for a bold, modern and clean/simple design that makes us stand out. We stand out as professionals in the industry and would like the stationery that our clients see to convey this image as well.

There is no colour preference.

We have used a "Lion" as our logo/symbol and that has received positive feedback from our clients; if you think the lion works then please incorporate the "lion".

If you think another symbol works then please submit this we are very open to ideas and would like to see designs that don't incorporate a lion as well.

We would like a corporate feel to this.

You could also incorporate the LG logo http://www.ledgerguildexample.com.au/Members/Marketing-your-practice/Logos but this is not a must.

WHO WE ARE:-
We are a Chartered Accounting firm who specialise in the delivery of taxation and strategic insolvency services. We also provide financial reporting services that help clients negotiate and compromise their debt or expenses such as rent with their landlords.

We work with Law Firms, other Accountants to deliver the best service for our clients.

Our clients come from varied backgrounds and are largely successful and established businesses and high net worth individuals looks for effective tax planning.

We are not the usual accounting firm and do not provide traditional tax return based services.
Updates

Target Market(s)

Corporate/ Independent successful businesses and individuals

Industry/Entity Type

Business

Requirements
Must have
• The letter must have the following phrase
“Liability limited by a scheme approved under Professional Standards Legislation”

The letter must also have the following business information:-
“The Pellow Group Pty Ltd atf
Principal - Martin K. Pellow
ABN: 47 205 318 664”

Plus Usual Address & Contact Details

We would also a logo or symbol that is representative of us. We like the idea of a lion but this is not set in stone and are very open to ideas.

```html
<!DOCTYPE html>
<html lang="en">
<head>
<meta charset="utf-8">
<title>The Pellow Group — Stationery</title>
<link rel="stylesheet" href="https://fonts.googleapis.com/css2?family=Arimo:wght@400&family=Marcellus&display=swap">
<style>
  :root {
    --brand-red: #e8323a;
    --ink-grey: #4a4a4a;
    --soft-grey: #8a8a8a;
    --pale-grey: #e4e4e4;
    --band-grey: #8c8c8c;
    --paper: #ffffff;
    --backdrop: #eeeeee;
  }
  * { margin: 0; padding: 0; box-sizing: border-box; }
  html, body { width: 1200px; height: 895px; overflow: hidden; }
  body {
    position: relative;
    background: var(--backdrop);
    font-family: "Arimo", Arial, sans-serif;
    color: var(--ink-grey);
  }
  .piece { position: absolute; background: var(--paper); }

  .brand { position: absolute; text-align: center; color: var(--brand-red); font-family: "Arimo", Arial, sans-serif; font-weight: 400; }
  .brand-dot { display: block; margin: 0 auto; border-radius: 50%; background: var(--brand-red); }
  .brand-name { display: block; white-space: nowrap; }
  .brand-suffix { display: block; text-align: right; }

  .contact { font-family: "Marcellus", Georgia, serif; color: var(--ink-grey); }
  .slogan { position: absolute; font-family: "Marcellus", Georgia, serif; color: var(--soft-grey); letter-spacing: 0.08em; white-space: nowrap; }

  /* Business card front */
  .card-front { left: 38px; top: 60px; width: 310px; height: 169px; }
  .card-front .brand { left: 0; right: 0; top: 48px; margin: 0 auto; width: 152px; }
  .card-front .brand-dot { width: 28px; height: 28px; margin-bottom: 18px; }
  .card-front .brand-name { font-size: 19px; }
  .card-front .brand-suffix { font-size: 11px; margin-top: -2px; }
  .card-front .slogan { left: 0; right: 0; top: 140px; text-align: center; font-size: 9px; }

  /* Business card back */
  .card-back { left: 416px; top: 64px; width: 311px; height: 171px; }
  .card-back .holder-name { position: absolute; left: 24px; top: 36px; font-size: 16px; }
  .card-back .holder-role { position: absolute; left: 97px; top: 56px; font-size: 11px; }
  .card-back .corner-name { position: absolute; right: 14px; top: 16px; font-family: "Arimo", Arial, sans-serif; font-size: 11px; color: var(--soft-grey); }
  .card-back .address { position: absolute; left: 50px; top: 120px; font-size: 8.5px; text-align: center; line-height: 10px; }
  .card-back .address span { font-size: 7.5px; }
  .card-back .divider { position: absolute; left: 173px; top: 108px; width: 1.5px; height: 44px; background: var(--ink-grey); }
  .card-back .lines { position: absolute; left: 183px; top: 110px; font-size: 8px; line-height: 9.5px; }

  /* Disc */
  .disc { left: 797px; top: 154px; width: 368px; height: 368px; border-radius: 50%; }
  .disc .brand { left: 0; right: 0; top: 28px; margin: 0 auto; width: 152px; }
  .disc .brand-dot { width: 28px; height: 28px; margin-bottom: 18px; }
  .disc .brand-name { font-size: 19px; }
  .disc .brand-suffix { font-size: 11px; margin-top: -2px; }
  .disc .hub { position: absolute; left: 146px; top: 146px; width: 76px; height: 76px; border-radius: 50%; background: var(--pale-grey); }
  .disc .label { position: absolute; left: 110px; top: 292px; font-size: 26px; color: #6a6a6a; }

  /* Letterhead */
  .letterhead { left: 66px; top: 343px; width: 362px; height: 470px; }
  .letterhead .brand { left: 0; right: 0; top: 18px; margin: 0 auto; width: 100px; }
  .letterhead .brand-dot { width: 20px; height: 20px; margin-bottom: 8px; }
  .letterhead .brand-name { font-size: 13px; }
  .letterhead .brand-suffix { font-size: 7px; margin-top: -1px; }
  .letterhead .rule { position: absolute; left: 0; top: 76px; }
  .letterhead .slogan { left: 50px; top: 110px; font-size: 7px; }
  .letterhead .date { position: absolute; left: 290px; top: 106px; font-size: 10px; }
  .letterhead .body { position: absolute; left: 50px; top: 130px; width: 250px; font-size: 5.4px; line-height: 6.8px; color: var(--soft-grey); }
  .letterhead .body p { margin-bottom: 6.8px; }
  .letterhead .entity { position: absolute; left: 50px; top: 384px; font-size: 5.6px; line-height: 7.4px; color: var(--soft-grey); }
  .letterhead .liability { position: absolute; left: 0; right: 0; top: 420px; text-align: center; font-size: 5.6px; color: var(--soft-grey); font-style: normal; }
  .letterhead .footer { position: absolute; left: 0; right: 0; top: 440px; text-align: center; font-size: 8px; line-height: 11px; }

  /* With compliments slip */
  .compliments { left: 498px; top: 582px; width: 414px; height: 221px; border-radius: 22px 22px 0 0; overflow: hidden; }
  .compliments .flap-band { position: absolute; left: 0; top: 0; width: 100%; height: 45px; background: var(--brand-red); }
  .compliments .grey-band { position: absolute; left: 0; top: 45px; width: 100%; height: 8px; background: var(--band-grey); }
  .compliments .greeting { position: absolute; left: 24px; top: 72px; font-family: "Marcellus", Georgia, serif; font-size: 20px; color: var(--ink-grey); }
  .compliments .slogan { left: 24px; top: 100px; font-size: 8px; }
  .compliments .return { position: absolute; left: 17px; top: 193px; font-size: 6.6px; line-height: 9px; text-align: center; }
  .compliments .brand { right: 6px; top: 180px; width: 70px; }
  .compliments .brand-dot { width: 12px; height: 12px; margin-bottom: 3px; }
  .compliments .brand-name { font-size: 8.5px; }
  .compliments .brand-suffix { font-size: 5px; }
</style>
</head>
<body>

  <section class="piece card-front" aria-label="Business card, front">
    <div class="brand">
      <span class="brand-dot"></span>
      <span class="brand-name">The Pellow Group</span>
      <span class="brand-suffix">Pty Ltd</span>
    </div>
    <p class="slogan">Strategic Solutions</p>
  </section>

  <section class="piece card-back contact" aria-label="Business card, back">
    <span class="corner-name">The Pellow Group</span>
    <p class="holder-name">Daniel Hartley</p>
    <p class="holder-role">Director</p>
    <p class="address">Address: <span>Abc street, abc town</span><br><span>New York, USA</span></p>
    <span class="divider"></span>
    <p class="lines">Mob #0000-000-000<br>Phone # 000-000-0000<br>Fax # 00-0000-0000<br>Email Id: abc@abc.com</p>
  </section>

  <section class="piece disc" aria-label="Disc label">
    <div class="brand">
      <span class="brand-dot"></span>
      <span class="brand-name">The Pellow Group</span>
      <span class="brand-suffix">Pty Ltd</span>
    </div>
    <span class="hub"></span>
    <p class="label">Name Here</p>
  </section>

  <section class="piece letterhead" aria-label="Letterhead">
    <div class="brand">
      <span class="brand-dot"></span>
      <span class="brand-name">The Pellow Group</span>
      <span class="brand-suffix">Pty Ltd</span>
    </div>
    <svg class="rule" width="362" height="10" viewBox="0 0 362 10" aria-hidden="true">
      <polygon points="0,2 280,2 276,8 0,8" fill="#e8323a"/>
      <polygon points="290,2 362,2 362,7 284,7" fill="#e8323a"/>
    </svg>
    <p class="slogan">Strategic Solutions</p>
    <p class="date contact">Date:______</p>
    <div class="body">
      <p>Hello There,</p>
      <p>We thank you for the opportunity to review your current tax position and planning needs. Our team has prepared a short summary of the matters discussed at our recent meeting, along with the next steps we propose for the coming financial year. Each item has been set out in plain terms so that you can consider it at your convenience.</p>
      <p>It is our view that a structured approach will reduce your exposure and improve cash flow. We will work closely with your legal advisers and other accountants to ensure each recommendation is practical, timely and fully documented for your records. Where a negotiation with a landlord or creditor is needed, we will prepare the supporting reports.</p>
      <p>Please review the enclosed schedule and let us know of any changes to your circumstances. Once confirmed, we will arrange a follow-up meeting to finalise the plan and agree on the timing of each step.</p>
      <p>We look forward to continuing our work with you and your business over the year ahead.</p>
      <p>Best Regards,</p>
    </div>
    <p class="entity">The Pellow Group Pty Ltd atf<br>Principal - Martin K. Pellow<br>ABN: 47 205 318 664</p>
    <p class="liability">Liability limited by a scheme approved under Professional Standards Legislation</p>
    <p class="footer contact">Address: abc street, abc town New York, USA<br>Phone #0000-000-000 | Fax # 00-0000-0000| Email Id: abc@abc.com</p>
  </section>

  <section class="piece compliments" aria-label="With Compliments slip">
    <span class="flap-band"></span>
    <span class="grey-band"></span>
    <p class="greeting">With Compliments</p>
    <p class="slogan">Strategic Solutions</p>
    <p class="return contact">Address: abc street, abc town New York, USA<br>Phone #0000-000-000 | Fax # 00-0000-0000| Email Id: abc@abc.com</p>
    <div class="brand">
      <span class="brand-dot"></span>
      <span class="brand-name">The Pellow Group</span>
      <span class="brand-suffix">Pty Ltd</span>
    </div>
  </section>

</body>
</html>
```